Startup Drone Platform Company business card

We are needing a business card design for our employees. We are a startup drone platform. We are looking for a business card that has our logo on one side, with the employee/company details on the opposite side. We are looking for something that is very eye catching, modern, and bold.

Target Market(s)

This will target both drone pilots and drone businesses, along with all the industries that could utilize drone services (aerial video, aerial photos, inspections, 3d mapping, etc).

Industry/Entity Type

Business

```html
<!DOCTYPE html>
<html lang="en">
<head>
<meta charset="utf-8">
<title>Aerolift Business Card</title>
<link rel="stylesheet" href="https://fonts.googleapis.com/css2?family=Raleway:wght@500&family=Lato:wght@400&display=swap">
<style>
  :root {
    --page-bg: #e9e7e3;
    --card-black: #1c1c1e;
    --card-black-light: #2a2a2d;
    --panel-grey: #5a5a5e;
    --panel-grey-light: #6b6b70;
    --divider: #cfcfd2;
    --ink-white: #f4f4f4;
    --accent-teal: #4fc3c9;
    --icon-bg: #111113;
  }
  * { box-sizing: border-box; margin: 0; padding: 0; }
  html, body {
    width: 1200px;
    height: 675px;
    overflow: hidden;
    background: var(--page-bg);
  }
  .sheet {
    position: relative;
    width: 1200px;
    height: 675px;
  }
  .card {
    position: absolute;
    top: 188px;
    width: 520px;
    height: 300px;
    border-radius: 4px;
    overflow: hidden;
    background: linear-gradient(135deg, var(--card-black-light), var(--card-black) 60%);
    box-shadow: 0 10px 28px rgba(0,0,0,0.25);
  }
  .card--front { left: 60px; }
  .card--back  { left: 620px; }

  .wordmark {
    position: absolute;
    display: flex;
    align-items: center;
    gap: 14px;
    font-family: "Raleway", sans-serif;
    font-weight: 500;
    color: var(--ink-white);
    letter-spacing: 0.32em;
  }
  .wordmark__dot {
    width: 16px;
    height: 16px;
    border-radius: 50%;
    background: var(--accent-teal);
  }
  .card--front .wordmark {
    left: 50%;
    top: 50%;
    transform: translate(-50%, -50%);
    font-size: 30px;
  }
  .card--back .wordmark {
    left: 165px;
    top: 150px;
    transform: translate(-50%, -50%);
    font-size: 26px;
  }

  .back-panel {
    position: absolute;
    inset: 0;
  }

  .contacts {
    position: absolute;
    left: 360px;
    top: 56px;
    display: flex;
    flex-direction: column;
    gap: 30px;
    font-family: "Lato", sans-serif;
    font-size: 11.5px;
    line-height: 1.4;
    color: var(--ink-white);
  }
  .contact {
    display: flex;
    align-items: center;
    gap: 12px;
  }
  .contact__icon {
    flex: none;
    width: 28px;
    height: 28px;
    border-radius: 50%;
    background: var(--icon-bg);
    display: flex;
    align-items: center;
    justify-content: center;
  }
  .contact__icon svg { width: 14px; height: 14px; }
</style>
</head>
<body>
<main class="sheet">

  <section class="card card--front" aria-label="Card front">
    <div class="wordmark"><span class="wordmark__dot"></span>AEROLIFT</div>
  </section>

  <section class="card card--back" aria-label="Card back">
    <svg class="back-panel" viewBox="0 0 520 300" width="520" height="300" aria-hidden="true">
      <defs>
        <linearGradient id="panelShade" x1="0" y1="0" x2="1" y2="1">
          <stop offset="0" stop-color="var(--panel-grey-light)"/>
          <stop offset="1" stop-color="var(--panel-grey)"/>
        </linearGradient>
      </defs>
      <path d="M340 0 C 300 90, 300 200, 345 300 L520 300 L520 0 Z" fill="url(#panelShade)"/>
      <path d="M334 0 C 294 90, 294 200, 339 300" fill="none" stroke="var(--divider)" stroke-width="6"/>
    </svg>

    <div class="wordmark"><span class="wordmark__dot"></span>AEROLIFT</div>

    <div class="contacts">
      <div class="contact">
        <span class="contact__icon">
          <svg viewBox="0 0 24 24"><path fill="var(--ink-white)" d="M6.6 10.8a15.1 15.1 0 0 0 6.6 6.6l2.2-2.2a1 1 0 0 1 1-.25 11.4 11.4 0 0 0 3.6.57 1 1 0 0 1 1 1V20a1 1 0 0 1-1 1A17 17 0 0 1 3 4a1 1 0 0 1 1-1h3.5a1 1 0 0 1 1 1c0 1.25.2 2.45.57 3.6a1 1 0 0 1-.25 1z"/></svg>
        </span>
        <span>+1 234 567 8910<br>+1 234 567 8910</span>
      </div>
      <div class="contact">
        <span class="contact__icon">
          <svg viewBox="0 0 24 24"><rect x="3" y="5" width="18" height="14" rx="2" fill="none" stroke="var(--ink-white)" stroke-width="2"/><path d="M3 7l9 6 9-6" fill="none" stroke="var(--ink-white)" stroke-width="2"/></svg>
        </span>
        <span>your@e-mail.com<br>www.yourwebsite.com</span>
      </div>
      <div class="contact">
        <span class="contact__icon">
          <svg viewBox="0 0 24 24"><path fill="var(--ink-white)" d="M12 2a7 7 0 0 0-7 7c0 5.2 7 13 7 13s7-7.8 7-13a7 7 0 0 0-7-7zm0 9.5A2.5 2.5 0 1 1 12 6.5a2.5 2.5 0 0 1 0 5z"/></svg>
        </span>
        <span>Your Street name, City,<br>Country, Zip Code.</span>
      </div>
    </div>
  </section>

</main>
</body>
</html>
```